Letterhead to Introduce a 'Sister' Company.

What I am needing is a design for a letter head to introduce our current customers base of (KT Alarm) customers to our new service, 'Kestrel Tide Solar Brokers'

```html
<!DOCTYPE html>
<html lang="en">
<head>
<meta charset="utf-8">
<title>KT Alarm Letterhead</title>
<link href="https://fonts.googleapis.com/css2?family=Montserrat:wght@400;600;700;800&family=Encode+Sans+Condensed:wght@400&display=swap" rel="stylesheet">
<style>
  :root {
    --blue: #0a5599;
    --green: #4cb848;
    --orange: #f39c1e;
    --ink: #555555;
    --ink-dark: #5b5b5b;
    --paper: #ffffff;
  }
  * { margin: 0; padding: 0; box-sizing: border-box; }
  html, body { width: 1056px; height: 1200px; overflow: hidden; background: var(--paper); }
  .letterhead {
    position: relative;
    width: 1056px;
    height: 1200px;
    background: var(--paper);
    font-family: "Montserrat", sans-serif;
    color: var(--ink);
  }
  .brand-mark {
    position: absolute;
    left: 100px;
    top: 104px;
    display: flex;
    align-items: center;
    gap: 12px;
  }
  .brand-mark .dot {
    width: 22px; height: 22px; border-radius: 50%;
    background: var(--green);
  }
  .brand-mark .name {
    font-weight: 700;
    font-size: 40px;
    letter-spacing: 1px;
    color: var(--blue);
  }
  .contact {
    position: absolute;
    left: 728px;
    top: 70px;
    padding-left: 20px;
    border-left: 2px solid var(--blue);
    font-size: 17px;
    line-height: 1.3;
    font-style: normal;
    color: var(--ink);
  }
  .contact .address { margin-bottom: 8px; }
  .contact .row { display: flex; align-items: center; gap: 12px; height: 27px; }
  .contact svg { width: 22px; height: 22px; flex: none; }
  .recipient { position: absolute; left: 100px; top: 395px; }
  .recipient .date { font-size: 21px; color: var(--ink); }
  .recipient .person {
    font-weight: 800; font-size: 33px; color: var(--ink-dark);
    margin-top: 8px; letter-spacing: 0.3px;
  }
  .recipient .role { font-size: 21px; color: var(--ink); margin-top: 6px; }
  .letter-body {
    position: absolute;
    left: 100px;
    top: 545px;
    width: 864px;
    font-family: "Encode Sans Condensed", sans-serif;
    font-size: 21px;
    line-height: 31px;
    color: var(--ink);
    text-align: justify;
  }
  .letter-body p { margin-bottom: 22px; }
  .letter-body p:last-child { margin-bottom: 0; }
  .sign-off {
    position: absolute; left: 100px; top: 890px;
    font-family: "Encode Sans Condensed", sans-serif;
    font-size: 22px; color: var(--ink);
  }
  .signature {
    position: absolute; left: 100px; top: 930px;
    width: 115px; height: 62px;
    background: linear-gradient(135deg, #e3f1fa, #cbe6f6);
    border-radius: 4px;
  }
  .sister-brand {
    position: absolute;
    left: 775px;
    top: 1050px;
    width: 240px;
    text-align: center;
  }
  .sister-brand .dot {
    width: 46px; height: 46px; border-radius: 50%;
    background: var(--orange);
    margin: 0 auto 8px;
  }
  .sister-brand .name {
    font-weight: 700; font-size: 17px; line-height: 1.25;
    color: var(--blue);
  }
  .footer-bands { position: absolute; left: 0; bottom: 0; width: 1056px; height: 36px; }
</style>
</head>
<body>
<main class="letterhead">
  <div class="brand-mark">
    <span class="dot"></span>
    <span class="name">KT Alarm</span>
  </div>

  <address class="contact">
    <div class="address">PO Box 2710. Harbor Point,<br>WA 98000</div>
    <div class="row">
      <svg viewBox="0 0 24 24" aria-hidden="true"><circle cx="12" cy="12" r="10.5" fill="none" stroke="var(--blue)" stroke-width="2"/><path d="M8.5 7c.6-.5 1.2-.4 1.6.2l1 1.6c.3.5.2 1-.2 1.4l-.6.5c.5 1.2 1.6 2.3 2.8 2.9l.5-.6c.4-.4.9-.5 1.4-.2l1.6 1c.6.4.7 1 .2 1.6l-.8.8c-2.6 1.2-8-4.2-7.3-7.4z" fill="var(--blue)"/></svg>
      <span>555-014-2290</span>
    </div>
    <div class="row">
      <svg viewBox="0 0 24 24" aria-hidden="true"><circle cx="12" cy="12" r="10.5" fill="none" stroke="var(--blue)" stroke-width="2"/><rect x="6.5" y="8" width="11" height="8" fill="none" stroke="var(--blue)" stroke-width="1.5"/><path d="M6.5 8l5.5 4.5L17.5 8M6.5 16l4-3.5M17.5 16l-4-3.5" fill="none" stroke="var(--blue)" stroke-width="1.3"/></svg>
      <span>hello@kthomeguard.com</span>
    </div>
    <div class="row">
      <svg viewBox="0 0 24 24" aria-hidden="true"><circle cx="12" cy="12" r="10.5" fill="none" stroke="var(--blue)" stroke-width="2"/><circle cx="12" cy="12" r="6" fill="none" stroke="var(--blue)" stroke-width="1.3"/><ellipse cx="12" cy="12" rx="2.6" ry="6" fill="none" stroke="var(--blue)" stroke-width="1.2"/><path d="M6 12h12M7 9h10M7 15h10" stroke="var(--blue)" stroke-width="1"/></svg>
      <span>www.kthomeguard.com</span>
    </div>
  </address>

  <section class="recipient">
    <div class="date">10 December, 2021</div>
    <div class="person">NATHAN BROOKS</div>
    <div class="role">Cheif Executive Officer</div>
  </section>

  <section class="letter-body">
    <p>Contrary to popular belief, Lorem Ipsum is not simply random text. It has roots in a piece of classical Latin literature from 45 BC, making it over 2000 years old. Daniel Whitcombe, a Latin professor at Ashford-Vale College in Virginia, looked up one of the more obscure Latin words, consectetur.</p>
    <p>Lorem Ipsum comes from sections 1.10.32 and 1.10.33 of "de Finibus Bonorum et Malorum" (The Extremes of Good and Evil) by Varenius, written in 45 BC. This book is a treatise on the theory of ethics, very popular during the Renaissance. The first line of Lorem Ipsum.</p>
    <p>The standard chunk of Lorem Ipsum used since the 1500s is reproduced below for those interested.</p>
  </section>

  <div class="sign-off">Best Regards</div>
  <div class="signature" role="img" aria-label="Handwritten signature of the sender in blue ink"></div>

  <div class="sister-brand">
    <div class="dot"></div>
    <div class="name">Kestrel Tide<br>Solar Brokers</div>
  </div>

  <svg class="footer-bands" viewBox="0 0 1056 36" preserveAspectRatio="none" aria-hidden="true">
    <polygon points="0,8 718,8 712,14 0,14" fill="var(--green)"/>
    <rect x="0" y="26" width="1056" height="10" fill="var(--blue)"/>
    <polygon points="733,0 1056,0 1056,36 704,36" fill="var(--blue)"/>
  </svg>
</main>
</body>
</html>
```